Inspiring book cover design (business book for designers and innovators)

I'm writing my first book, to be published early next year. I'm struggling to come up with an inspiring book cover design. I need your help!

Information to be included on the cover:
Book Title: Bright maker's manual
Subtitle: Designing products and services that make sense
Author: Marieke Vollen
Optional (not sure yet if I should include this on the cover): with online toolset

The book will be a square, size 170 x 170 mm
In the uploaded file you can find some example pages from the inside of the book. The cover design should fit with the design style of the example pages. The cover should "jump out" from the shelve in a bookstore and should attract designers, innovators, product managers, developers, and startup founders to buy the book.
Publisher: www.quarlomedia.example

About the book:
Why do some products fail while others become a success? Why do so many companies launch crappy products and services that nobody wants? This book is both a guide to and a source of inspiration for, designing products and services that make sense. Because if they make sense to people, people will want them.
In order for tech products and services to make sense, and create value for users, we need to apply technologies in a meaningful way. We can achieve this by designing strong benefits and at the same time minimizing resistance users might have against new technologies.
This book offers a complete overview of how to develop products and services that make sense: 27 ways to strengthen benefits and 28 ways to mitigate resistance. It offers practical insights, examples, tips, and tools to design products and services that people will love to use.

About the author:
https://www.profilehub.example/in/mariekevollen/

Target Market(s)

designers, innovators, product managers, developers, and startup founders

Industry/Entity Type

Design Agency

Font styles to use
Other font styles liked:
• You can choose. The inside of the book uses 3 fonts: LuloCleanW01-OneBold, Sansation, Segoe UI

Requirements
Must have
• Clean, yet creative design.
Square shape
Fits the design style of the example pages
Sans serif fonts. Do not have to be the same fonts like the ones that are used inside the book (LuloCleanW01-OneBold, Sansation, Segoe UI), but should go well with them.

Bright makers manual
60 routes to build products and tools that feel right
Marieke Vollen
Nice to have
• I have several ideas that you might take as a starting point:
1) Do something with the left brain (rational, more digital) - right brain (creative, more emotional). For products to make sense, it needs to appeal to both parts of the brain
2) Work with a pattern, for example a (polygonal) triangular pattern
3) playful element in the letters, for example turning the O in innovator's into an on-off button or a stylish smiley, flipping the N in innovator's, doing something playful with the ' in innovator's
I've uploaded some images as a source of inspiration.

The cover should have a different color than the red/blue used in the example pages, but should fit the color palette that is used in the example pages.
Trigger curiosity.
Should not have
• Photographic pictures

```html
<!DOCTYPE html>
<html lang="en">
<head>
<meta charset="utf-8">
<title>Bright makers manual — book cover</title>
<link rel="stylesheet" href="https://fonts.googleapis.com/css2?family=Montserrat:wght@300;700;900&display=swap">
<style>
  :root {
    --cover-red: #8c1222;
    --cover-red-deep: #6a0b17;
    --cover-red-glow: #b8182c;
    --band-dark: #3f0a11;
    --ink-light: #ffffff;
    --dot-line: rgba(255, 255, 255, 0.9);
  }
  * { margin: 0; padding: 0; box-sizing: border-box; }
  html, body {
    width: 1200px;
    height: 1200px;
    overflow: hidden;
    background: var(--cover-red-deep);
  }
  .cover {
    position: relative;
    width: 1200px;
    height: 1200px;
    overflow: hidden;
    background:
      radial-gradient(circle at 560px 680px, var(--cover-red-glow) 0%, rgba(184, 24, 44, 0) 45%),
      linear-gradient(160deg, var(--cover-red) 0%, var(--cover-red-deep) 100%);
  }
  .cover-art {
    position: absolute;
    inset: 0;
    width: 1200px;
    height: 1200px;
  }
  .book-title {
    position: absolute;
    left: 80px;
    top: 88px;
    font-family: "Montserrat", sans-serif;
    font-weight: 900;
    font-size: 104px;
    line-height: 122px;
    letter-spacing: 5px;
    color: var(--ink-light);
    text-transform: uppercase;
  }
  .book-title span { display: block; }
  .subtitle {
    position: absolute;
    left: 542px;
    top: 572px;
    font-family: "Montserrat", sans-serif;
    font-weight: 300;
    font-size: 54px;
    line-height: 80px;
    color: var(--ink-light);
  }
  .subtitle span { display: block; white-space: nowrap; }
  .author-band {
    position: absolute;
    left: 0;
    top: 1090px;
    width: 1200px;
    height: 66px;
    background: var(--band-dark);
    display: flex;
    align-items: center;
    justify-content: center;
  }
  .author-name {
    font-family: "Montserrat", sans-serif;
    font-weight: 700;
    font-size: 36px;
    letter-spacing: 5px;
    color: var(--ink-light);
    text-transform: uppercase;
  }
</style>
</head>
<body>
  <main class="cover">
    <svg class="cover-art" viewBox="0 0 1200 1200" xmlns="http://www.w3.org/2000/svg">
      <defs>
        <radialGradient id="globe-tone" cx="0.5" cy="0.5" r="0.5">
          <stop offset="0" stop-color="#c02a3c" stop-opacity="0.55"/>
          <stop offset="1" stop-color="#8c1222" stop-opacity="0"/>
        </radialGradient>
        <radialGradient id="hand-tone" cx="0.5" cy="0.5" r="0.5">
          <stop offset="0" stop-color="#c9485a" stop-opacity="0.5"/>
          <stop offset="1" stop-color="#8c1222" stop-opacity="0"/>
        </radialGradient>
      </defs>
      <ellipse role="img" aria-label="Dotted digital globe illustration" cx="300" cy="880" rx="620" ry="520" fill="url(#globe-tone)"/>
      <ellipse role="img" aria-label="Polygonal wireframe hand illustration" cx="900" cy="430" rx="300" ry="220" fill="url(#hand-tone)"/>
      <circle class="subtitle-ring" cx="754" cy="734" r="320" fill="none" stroke="var(--dot-line)" stroke-width="4" stroke-linecap="round" stroke-dasharray="0.1 13"/>
    </svg>

    <h1 class="book-title">
      <span>Bright</span>
      <span>Makers</span>
      <span>Manual</span>
    </h1>

    <p class="subtitle">
      <span>60 routes to</span>
      <span>build products</span>
      <span>and tools that</span>
      <span>feel right</span>
    </p>

    <div class="author-band">
      <p class="author-name">Marieke Vollen</p>
    </div>
  </main>
</body>
</html>
```